Seeds of Renewal needs a business card design

I need a business card design for my company to promote my new Christian non-fiction book, "Where the Quiet River Bends." I also want it to promote my web site, www.seedsofrenewalway.com. The book is about empowering people to be transformed through a deeper relationship with God. I am picturing a design with a dove over water that matches the colors of my book cover, blue, white, yellow, and orange. Fire and light would also be possible elements of the design. I would like to be able to use the dove by itself as a logo for my business. This is my first book and I do not know if others will follow. The name of my publishing company is Lantern Valley Press, named after Gideon in the Bible story from the book of Judges. My book was independently published and was recently selected as a finalist for the 2015 Bright Horizon SMALLPRESS book prize in the Christian non-fiction genre.

Target Market(s)

People who are hungry for more of God and who want to experience deep change in their lives.

Industry/Entity Type

Business

Contact Information for Business Card

Dana Whitfield
Author
Where the Quiet River Bends
4283 Maple Hollow Lane
Austin, Texas 78952-1184
512-555-0147 512-555-0193
dana-whitfield@brightmailbox.net
www.seedsofrenewalway.com

Colors
0355a3
3377b5
85acd3
cedeed
fbee3e
ffc214

Requirements
Must have
• A dove with a blue background, peaceful and appealing
Nice to have
• Water and fire or light
Should not have
• Violence or fear-producing images

```html
<!DOCTYPE html>
<html lang="en">
<head>
<meta charset="utf-8">
<title>Dana Whitfield – Business Card</title>
<link rel="stylesheet" href="https://fonts.googleapis.com/css2?family=Montserrat:wght@500&family=Tinos&display=swap">
<style>
  :root {
    --page: #ffffff;
    --backdrop: #b5b2b1;
    --navy: #001f4f;
    --title-navy: #0b2559;
    --water-light: #4a72b4;
    --water-deep: #2d4f90;
    --white: #ffffff;
  }
  html, body {
    margin: 0;
    width: 1200px;
    height: 1000px;
    overflow: hidden;
    background: var(--page);
  }
  .backdrop {
    position: absolute;
    left: 49px; top: 38px;
    width: 1110px; height: 935px;
    background: var(--backdrop);
  }
  .card {
    position: absolute;
    left: 279px; top: 339px;
    width: 651px; height: 371px;
    overflow: hidden;
    background: var(--navy);
  }
  .card-art { position: absolute; inset: 0; }
  .dove-mark {
    position: absolute;
    left: 190px; top: 30px;
    width: 115px; height: 125px;
    border-radius: 50%;
    background: radial-gradient(circle, rgba(255,255,255,0.95) 0%, rgba(255,255,255,0.55) 35%, rgba(255,255,255,0) 70%);
  }
  .identity {
    position: absolute;
    left: 440px; top: 18px;
    width: 188px;
    text-align: center;
    font-family: "Montserrat", sans-serif;
    font-weight: 500;
    color: var(--white);
  }
  .identity .name { font-size: 19px; line-height: 24px; }
  .identity .role { font-size: 16px; line-height: 19px; margin-left: 14px; }
  .contact {
    position: absolute;
    left: 368px; top: 72px;
    font-family: "Montserrat", sans-serif;
    font-weight: 500;
    font-size: 14px;
    color: var(--white);
  }
  .contact p { margin: 0; line-height: 18px; }
  .contact .address { margin-bottom: 13px; }
  .contact .phones { margin-bottom: 14px; }
  .contact .phones .rule {
    display: inline-block;
    width: 1px; height: 20px;
    background: var(--white);
    vertical-align: -5px;
    margin: 0 8px;
  }
  .contact .email { margin-bottom: 13px; }
  .book-title {
    position: absolute;
    left: 144px; top: 258px;
    margin: 0;
    font-family: "Tinos", serif;
    font-weight: 400;
    font-size: 32px;
    line-height: 38px;
    color: var(--title-navy);
  }
</style>
</head>
<body>
  <div class="backdrop"></div>
  <section class="card">
    <svg class="card-art" width="651" height="371" viewBox="0 0 651 371">
      <defs>
        <linearGradient id="sea" x1="0" y1="0" x2="0" y2="1">
          <stop offset="0" stop-color="var(--water-deep)"/>
          <stop offset="1" stop-color="var(--water-light)"/>
        </linearGradient>
      </defs>
      <path role="img" aria-label="Photo of ocean waves splashing against rocks"
            d="M0,112 C140,165 260,222 430,262 C560,292 630,330 645,371 L0,371 Z" fill="url(#sea)"/>
      <path class="swoosh" fill="var(--white)"
            d="M0,56 C160,122 260,190 430,225 C560,254 640,292 651,342 L651,371 C630,322 560,280 430,250 C260,213 140,152 0,95 Z"/>
    </svg>
    <div class="dove-mark" role="img" aria-label="Glowing white dove in flight"></div>
    <div class="identity">
      <div class="name">Dana Whitfield</div>
      <div class="role">Author</div>
    </div>
    <div class="contact">
      <p class="address">4283 Maple Hollow Lane Austin,<br>Texas&nbsp; 78952-1184</p>
      <p class="phones">T :&nbsp; 512-555-0147<span class="rule"></span>512-555-0193</p>
      <p class="email">dana-whitfield@brightmailbox.net</p>
      <p class="web">www.seedsofrenewalway.com</p>
    </div>
    <h1 class="book-title">Where the Quiet<br>River Bends</h1>
  </section>
</body>
</html>
```